Law Firm Needs Brochure Redesign Using New Logo

We are a personal injury law firm that does auto injuries and other personal injury cases. We want a new brochure that has our updated logo and information. Instead of gold and black, we want more navy, as matches the new logo. The Auto Liability portion should read: "(required by the state of Arizona in the amounts of $25,000 per person / $50,000 per accident, but a higher amount may be best )." The other information can remain the same. We'd like the brochure to keep the same professional tone as the previous brochure.
Our website is https://www.brandtlegalpartners.example/.

```html
<!DOCTYPE html>
<html lang="en">
<head>
<meta charset="utf-8">
<title>Brandt Legal – Car Accident Brochure</title>
<link href="https://fonts.googleapis.com/css2?family=Montserrat:wght@400;500;600;700;800;900&display=swap" rel="stylesheet">
<style>
  :root{
    --navy:#1b2a44;
    --navy-deep:#0f1a2e;
    --navy-mid:#27395a;
    --steel:#8b929d;
    --steel-light:#b9bec6;
    --ice:#9fc3ea;
    --white:#ffffff;
    --paper:#eef0f3;
    --ink:#1b2a44;
  }
  *{box-sizing:border-box;margin:0;padding:0}
  html,body{width:1200px;height:2776px;overflow:hidden}
  body{background:var(--paper);font-family:"Montserrat",Arial,sans-serif;color:var(--white);position:relative}
  .spread{position:absolute;left:40px;width:1120px;height:820px;box-shadow:0 10px 30px rgba(15,26,46,.18);display:flex}
  .spread--outside{top:538px}
  .spread--inside{top:1418px}
  .panel{position:relative;width:373.33px;height:100%;overflow:hidden}
  .photo{position:absolute;left:0;width:100%}

  /* outside: stats panel */
  .stats{background:var(--navy-deep)}
  .stats .photo{top:0;height:100%;background:linear-gradient(180deg,#1d2b45 0%,#243553 45%,#3a4a62 70%,#1a2438 100%)}
  .stats-block{position:absolute;left:40px;right:30px}
  .stats-block--first{top:50px}
  .stats-block--second{top:235px}
  .stat-over{font-size:22px;font-weight:600;letter-spacing:1px}
  .stat-number{font-size:58px;font-weight:800;line-height:1}
  .stat-note{font-size:16px;font-weight:500;margin-top:8px;line-height:1.35}
  .promise-box{position:absolute;left:40px;right:40px;bottom:40px;height:200px;background:rgba(139,146,157,.88);padding:26px 22px;font-size:13px;line-height:1.55;font-weight:500}

  /* outside: back panel */
  .back{background:var(--white)}
  .back-mark{position:absolute;left:40px;bottom:60px;transform-origin:left bottom;transform:rotate(-90deg) translateY(100%);width:430px;display:flex;align-items:center;gap:16px}
  .back-address{color:var(--navy);font-size:14px;font-weight:600;line-height:1.5}

  .brand{display:flex;align-items:center;gap:10px;color:var(--navy)}
  .brand-square{width:26px;height:26px;background:var(--navy)}
  .brand-name{font-weight:800;font-size:26px;letter-spacing:.5px;white-space:nowrap}

  /* outside: cover */
  .cover{background:var(--navy)}
  .cover-head{position:absolute;top:0;left:0;right:0;height:110px;background:var(--white);display:flex;align-items:center;justify-content:flex-end;padding-right:28px}
  .cover .photo{top:110px;height:230px;background:linear-gradient(180deg,#c9ccd2 0%,#6b7280 40%,#1c2232 75%,#0f1a2e 100%)}
  .cover-text{position:absolute;top:380px;left:0;right:0;text-align:center;padding:0 20px}
  .cover-kicker{font-size:21px;font-weight:700;line-height:1.25;letter-spacing:.5px}
  .cover-title{font-size:48px;font-weight:900;line-height:1.02;margin-top:10px;white-space:nowrap}
  .cover-title .cover-title-big{display:block;font-size:64px}
  .cover-sub{font-size:18px;font-weight:500;margin-top:16px;line-height:1.35}
  .cover-url{position:absolute;bottom:38px;left:0;right:0;text-align:center;font-size:12px;font-weight:600;color:var(--steel-light)}

  /* inside: tips */
  .tips{background:var(--navy)}
  .tips-title{position:absolute;top:38px;left:32px;font-size:26px;font-weight:800;line-height:1.1}
  .tips-title span{display:block;font-size:15px;font-weight:600;color:var(--steel-light);margin-top:4px}
  .tips-list{position:absolute;top:120px;left:32px;right:26px;list-style:none}
  .tips-list li{display:flex;gap:12px;align-items:flex-start;margin-bottom:10px;font-size:11.5px;line-height:1.35;font-weight:500}
  .tip-num{flex:0 0 30px;height:30px;border-radius:50%;background:var(--steel);display:flex;align-items:center;justify-content:center;font-weight:700;font-size:11px}
  .tips .photo{bottom:0;height:150px;background:linear-gradient(180deg,#27395a 0%,#1a2438 60%,#0c1322 100%)}

  /* inside: coverage */
  .coverage{background:var(--navy-deep)}
  .coverage .photo{top:0;height:260px;background:linear-gradient(180deg,#2b3c5c 0%,#1b2a44 60%,#0f1a2e 100%)}
  .coverage-icon{position:absolute;top:92px;left:50%;transform:translateX(-50%)}
  .coverage-title{position:absolute;top:280px;left:34px;font-size:18px;font-weight:600;line-height:1}
  .coverage-title strong{display:block;font-size:34px;font-weight:800;margin-top:4px}
  .coverage-list{position:absolute;top:365px;left:34px;right:28px}
  .coverage-item{margin-bottom:16px}
  .coverage-item h3{font-size:13px;font-weight:700;letter-spacing:.5px;color:var(--ice);margin-bottom:4px}
  .coverage-item p{font-size:11.5px;line-height:1.45;font-weight:500}

  /* inside: behaviour & contact */
  .behaviour{background:var(--navy)}
  .behaviour-head{position:absolute;left:32px;right:28px;font-size:30px;font-weight:800;line-height:1.05}
  .behaviour-head--model{top:40px}
  .behaviour-head--text{top:210px}
  .behaviour-copy{position:absolute;left:32px;right:28px;font-size:12px;line-height:1.45;font-weight:500}
  .behaviour-copy--model{top:120px;color:var(--steel-light)}
  .behaviour-copy--text{top:290px;color:var(--steel-light)}
  .behaviour-copy--strong{top:345px;font-weight:700}
  .behaviour .photo{top:420px;height:160px;background:linear-gradient(180deg,#3a4a62 0%,#27395a 55%,#1b2a44 100%)}
  .contact{position:absolute;left:40px;right:40px;bottom:36px;height:200px;background:var(--steel);padding:22px 20px;text-align:center}
  .contact h3{font-size:20px;font-weight:800}
  .contact-firm{font-size:14px;font-weight:600;margin-top:6px}
  .contact-line{display:flex;align-items:center;justify-content:center;gap:8px;font-size:13px;font-weight:500;margin-top:14px}
  .contact-address{font-size:12px;line-height:1.45;margin-top:10px;font-weight:500}
</style>
</head>
<body>

<section class="spread spread--outside" aria-label="Brochure outside spread">
  <div class="panel stats">
    <div class="photo" role="img" aria-label="Photograph of a highway stretching into the distance under a dusky sky"></div>
    <div class="stats-block stats-block--first">
      <div class="stat-over">OVER</div>
      <div class="stat-number">107,000</div>
      <p class="stat-note">crashes will happen in the state of Arizona this year.</p>
    </div>
    <div class="stats-block stats-block--second">
      <div class="stat-over">OVER</div>
      <div class="stat-number">700</div>
      <p class="stat-note">of them will result in fatalities.</p>
    </div>
    <div class="promise-box">If we don't see you, you don't pay attorney fees. Our team works to protect injured families across Arizona and helps them recover after a serious crash on the road.</div>
  </div>

  <div class="panel back">
    <div class="back-mark">
      <div class="brand"><span class="brand-square"></span><span class="brand-name">BRANDT LEGAL</span></div>
      <div class="back-address">4410 W. Canyon Road Suite 310<br>Phoenix AZ 85021</div>
    </div>
  </div>

  <div class="panel cover">
    <div class="cover-head">
      <div class="brand"><span class="brand-square"></span><span class="brand-name">BRANDT LEGAL</span></div>
    </div>
    <div class="photo" role="img" aria-label="Photograph of a dark luxury sports car on a road"></div>
    <div class="cover-text">
      <p class="cover-kicker">PROTECT YOUR<br>FAMILY IN CASE OF A</p>
      <h1 class="cover-title"><span class="cover-title-big">CAR</span>ACCIDENT</h1>
      <p class="cover-sub">A little knowledge and<br>preparation go a long way</p>
    </div>
    <div class="cover-url">https://www.brandtlegalpartners.example/</div>
  </div>
</section>

<section class="spread spread--inside" aria-label="Brochure inside spread">
  <div class="panel tips">
    <h2 class="tips-title">TOP 10 TIPS<span>TO AVOID A CRASH</span></h2>
    <ol class="tips-list">
      <li><span class="tip-num">01</span>Don't drive distracted. Keep your phone away and eyes on the road.</li>
      <li><span class="tip-num">02</span>Watch your speed and slow down in poor weather.</li>
      <li><span class="tip-num">03</span>Keep a safe following distance from the car ahead.</li>
      <li><span class="tip-num">04</span>Never drive after drinking or when you feel drowsy.</li>
      <li><span class="tip-num">05</span>Check mirrors and blind spots before every lane change.</li>
      <li><span class="tip-num">06</span>Obey traffic signals and come to full stops.</li>
      <li><span class="tip-num">07</span>Be cautious at intersections, even on a green light.</li>
      <li><span class="tip-num">08</span>Keep your vehicle maintained, with good tires and brakes.</li>
      <li><span class="tip-num">09</span>Always wear your seat belt and buckle up children.</li>
      <li><span class="tip-num">10</span>Plan your route ahead so you are not rushed.</li>
    </ol>
    <div class="photo" role="img" aria-label="Photograph of a dark car driving at dusk"></div>
  </div>

  <div class="panel coverage">
    <div class="photo" role="img" aria-label="Photograph of a businessperson's hands held protectively over a car"></div>
    <svg class="coverage-icon" width="70" height="80" viewBox="0 0 70 80" aria-hidden="true">
      <path d="M35 4 L64 14 V38 C64 58 50 70 35 76 C20 70 6 58 6 38 V14 Z" fill="#2f6fb8" stroke="#ffffff" stroke-width="3"/>
      <path d="M20 44 L24 34 H46 L50 44 V52 H20 Z" fill="#ffffff"/>
      <circle cx="27" cy="53" r="4" fill="#2f6fb8"/><circle cx="43" cy="53" r="4" fill="#2f6fb8"/>
    </svg>
    <h2 class="coverage-title">HAVE THE RIGHT<strong>COVERAGE</strong></h2>
    <div class="coverage-list">
      <div class="coverage-item"><h3>AUTO LIABILITY</h3><p>(required by the state of Arizona in the amounts of $25,000 per person / $50,000 per accident, but a higher amount may be best).</p></div>
      <div class="coverage-item"><h3>UNINSURED OR UNDERINSURED MOTORIST COVERAGE</h3><p>Protects you when the other driver doesn't have insurance or not enough.</p></div>
      <div class="coverage-item"><h3>MEDICAL PAYMENTS COVERAGE</h3><p>Up to $5,000 in coverage will be paid to you by your insurer for medical bills after a crash.</p></div>
      <div class="coverage-item"><h3>HOMEOWNER / RENTERS INSURANCE</h3><p>Protects you in case of injuries to your property or guests at your home.</p></div>
    </div>
  </div>

  <div class="panel behaviour">
    <h2 class="behaviour-head behaviour-head--model">MODEL SAFE<br>BEHAVIOR</h2>
    <p class="behaviour-copy behaviour-copy--model">Kids learn by watching. Show them how to drive with care and patience on every trip.</p>
    <h2 class="behaviour-head behaviour-head--text">NEVER TEXT<br>WHILE DRIVING</h2>
    <p class="behaviour-copy behaviour-copy--text">Studies show teens that text while driving are far more likely to crash.</p>
    <p class="behaviour-copy behaviour-copy--strong">When your children see you text, they learn it is more important than safety.</p>
    <div class="photo" role="img" aria-label="Photograph of hands holding a phone over a steering wheel"></div>
    <div class="contact">
      <h3>Contact Us</h3>
      <p class="contact-firm">Brandt Legal Group</p>
      <p class="contact-line">
        <svg width="14" height="14" viewBox="0 0 24 24" aria-hidden="true"><path d="M6.6 10.8a15 15 0 0 0 6.6 6.6l2.2-2.2a1 1 0 0 1 1-.25 11.4 11.4 0 0 0 3.6.57 1 1 0 0 1 1 1V20a1 1 0 0 1-1 1A17 17 0 0 1 3 4a1 1 0 0 1 1-1h3.5a1 1 0 0 1 1 1c0 1.25.2 2.45.57 3.57a1 1 0 0 1-.25 1z" fill="#ffffff"/></svg>
        (555) 014-2290
      </p>
      <p class="contact-address">4410 W. Canyon Road Suite 310<br>Phoenix AZ 85021</p>
    </div>
  </div>
</section>

</body>
</html>
```